National Human Immunology Network Needs a Brochure DesignBrochure Design Project

We need a brochure design for a new Canadian network called VOLT. VOLT stands for "Pemberly Human Immunology Network". (PMRT is the Northvale Councils of Wellness Study and is the funder of the network).

The Pemberly Human Immunology Network (VOLT) is a resource network that facilitates, promotes and enhances research in human immunology and its translation into clinical care and public policy. VOLT is an inclusive National Network with International projections that will act as a coordinating resource for investigators working in different aspects of Human Immunology. As a research network, VOLT will operate as a resource “umbrella” network, facilitating communication between nodes, each with their specialized expertise in human immunology,
collaboration and knowledge exchange.

We have a VOLT logo already designed as well as the text to be used in the brochure. In addition we should include the PMRT logo somewhere on the brochure, but it does need to be front and centre. Thinking that a tri-fold brochure would work best.

Target Market(s)

Researchers, politicians, lay public

Industry/Entity Type

Communication

Requirements
Must have
• Must use logo provided.

```html
<!DOCTYPE html>
<html lang="en">
<head>
<meta charset="utf-8">
<title>VOLT Tri-fold Brochure</title>
<link href="https://fonts.googleapis.com/css2?family=Open+Sans:wght@400;600;700&display=swap" rel="stylesheet">
<style>
  :root {
    --blue: #1b8fd6;
    --blue-light: #4fb6ea;
    --red: #b3121b;
    --ink: #3a3a3a;
    --paper: #ffffff;
    --stage: #e4e6e9;
  }
  * { box-sizing: border-box; margin: 0; padding: 0; }
  html, body { width: 1200px; height: 1004px; overflow: hidden; }
  body {
    background: var(--stage);
    font-family: "Open Sans", Arial, sans-serif;
    color: var(--ink);
  }
  .brochure {
    position: absolute; left: 90px; top: 107px;
    width: 1020px; height: 790px;
    display: flex;
    box-shadow: 0 6px 24px rgba(0,0,0,.18);
  }
  .panel { position: relative; width: 340px; height: 790px; overflow: hidden; }

  /* Inside flap */
  .panel--flap {
    background: linear-gradient(180deg, var(--blue-light) 0%, var(--blue) 55%, #1f9be0 100%);
    color: #fff;
  }
  .flap__tab {
    position: absolute; top: 0; right: 0; width: 200px; height: 34px;
    background: var(--red); border-bottom-left-radius: 18px;
    font-size: 15px; font-weight: 600; padding: 6px 16px;
  }
  .flap__body { position: absolute; top: 54px; left: 26px; right: 24px; font-size: 11.5px; line-height: 1.55; }
  .flap__body p { margin-bottom: 8px; }
  .flap__body ul { list-style: none; margin-bottom: 12px; }
  .flap__body li { padding-left: 10px; position: relative; margin-bottom: 3px; }
  .flap__body li::before { content: "•"; position: absolute; left: 0; }
  .flap__subhead { font-weight: 600; text-decoration: underline; margin: 6px 0; }
  .flap__photo {
    position: absolute; left: 0; right: 0; bottom: 0; height: 120px;
    background: linear-gradient(180deg, rgba(255,255,255,0) 0%, #8fd0f2 60%, #b9e2f6 100%);
  }

  /* Back panel */
  .panel--back { background: var(--paper); }
  .back__frame { position: absolute; inset: 18px; border: 1.5px solid var(--blue); }
  .back__title {
    position: absolute; top: 34px; left: 36px; right: 36px;
    color: var(--blue); font-size: 24px; font-weight: 600;
    border-bottom: 2px solid var(--blue); padding-bottom: 4px;
  }
  .back__photo {
    position: absolute; top: 84px; left: 36px; right: 36px; height: 240px;
    background: linear-gradient(135deg, #cfe7f6 0%, #7fb6de 45%, #3d7fb8 100%);
  }
  .back__badge {
    position: absolute; right: 36px; top: 254px; width: 140px; height: 70px;
    background: var(--blue);
    display: flex; align-items: center; justify-content: center;
  }
  .contacts { position: absolute; top: 360px; left: 44px; right: 36px; font-size: 12.5px; line-height: 1.5; }
  .contacts__item { margin-bottom: 14px; }
  .contacts__role { color: var(--blue); font-size: 14px; font-weight: 600; }
  .contacts__name { color: var(--ink); font-weight: 400; }
  .back__logo { position: absolute; left: 44px; bottom: 52px; }

  /* Cover */
  .panel--cover { background: var(--paper); }
  .cover__hero {
    position: absolute; top: 0; left: 0; right: 0; height: 360px;
    background: linear-gradient(160deg, #2a8fd8 0%, #1467b8 55%, #0d4f95 100%);
  }
  .cover__title { position: absolute; top: 110px; left: 34px; color: #fff; font-size: 34px; line-height: 1.12; font-weight: 400; }
  .cover__tagline { color: #cfe6f7; font-size: 13px; margin-top: 4px; }
  .cover__band {
    position: absolute; top: 360px; left: 0; right: 0; height: 38px;
    background: var(--red); color: #fff; font-size: 15px; padding: 8px 30px;
  }
  .cover__photo {
    position: absolute; top: 398px; left: 0; right: 0; height: 250px;
    background: linear-gradient(120deg, #e8eef3 0%, #b7c9d8 50%, #6f8ea8 100%);
  }
  .cover__logo { position: absolute; left: 40px; bottom: 58px; }

  /* Name lockup: plain square + name in one weight, one colour */
  .lockup { display: flex; align-items: center; gap: 10px; }
  .lockup__mark { width: 16px; height: 16px; background: var(--red); flex: none; }
  .lockup__name { font-size: 24px; font-weight: 600; color: var(--red); }
  .lockup--small .lockup__mark { width: 11px; height: 11px; }
  .lockup--small .lockup__name { font-size: 16px; }
  .lockup--reverse .lockup__mark { background: #fff; }
  .lockup--reverse .lockup__name { color: #fff; }
</style>
</head>
<body>
<main class="brochure">

  <section class="panel panel--flap">
    <div class="flap__tab">Accomplishments:</div>
    <div class="flap__body">
      <p>In its first year of operation, VOLT has made significant strides in the establishment of the network. Accomplishments to date include:</p>
      <ul>
        <li>Completion of set-up of the administrative centre and staffing</li>
        <li>Launch of the VOLT website</li>
        <li>Kick-off meeting of the node leaders in December 2011 and regular monthly calls</li>
        <li>Organization of a satellite symposium on human immunology at Immunity Forum 2012</li>
        <li>Creation of an External Advisory Board to provide advice and guidance to the network</li>
      </ul>
      <p class="flap__subhead">Next Steps:</p>
      <p>As VOLT moves forward into the second year of operation, plans are in the works for expanding the network. In addition, a series of meetings and conferences will be arranged to increase the profile of the network across the country and to engage trainees and fellows in human immunology.</p>
      <p>Finally, a focus on training will be supported by PMRT and the Northvale Councils of Wellness Study.</p>
    </div>
    <div class="flap__photo" role="img" aria-label="Photo of laboratory glassware in soft blue tones"></div>
  </section>

  <section class="panel panel--back">
    <div class="back__frame"></div>
    <h2 class="back__title">Lorem Ipsum</h2>
    <div class="back__photo" role="img" aria-label="Photo of a researcher working with laboratory equipment"></div>
    <div class="back__badge">
      <div class="lockup lockup--small lockup--reverse">
        <span class="lockup__mark"></span>
        <span class="lockup__name">VOLT</span>
      </div>
    </div>
    <div class="contacts">
      <div class="contacts__item">
        <div class="contacts__role">Director: <span class="contacts__name">Adrian Kessold</span></div>
        <div>Tel: 555-310-4821</div>
        <div>Email: a.kessold@harlowe.edu</div>
      </div>
      <div class="contacts__item">
        <div class="contacts__role">Manager: <span class="contacts__name">Marisa Tellwyn</span></div>
        <div>Tel: 555-742-1906</div>
        <div>Email: m.tellwyn@brantmoor.edu</div>
      </div>
      <div class="contacts__item">
        <div class="contacts__role">Mailing Address:</div>
        <div>Brantmoor Centre for Immunology</div>
        <div>88 Orchard Lane, Suite 5</div>
        <div>Brantmoor University</div>
        <div>Fairhaven, ZZ 00000</div>
      </div>
    </div>
    <div class="back__logo">
      <div class="lockup lockup--small">
        <span class="lockup__mark"></span>
        <span class="lockup__name">VOLT</span>
      </div>
    </div>
  </section>

  <section class="panel panel--cover">
    <div class="cover__hero" role="img" aria-label="Blue-toned photo of laboratory work"></div>
    <h1 class="cover__title">Lorem<br>Lorem Ipsum<div class="cover__tagline">Lorem ipsum dolor</div></h1>
    <div class="cover__band">Lorem ipsum dolor sit amet</div>
    <div class="cover__photo" role="img" aria-label="Photo of a scientist in mask and goggles examining a test tube"></div>
    <div class="cover__logo">
      <div class="lockup">
        <span class="lockup__mark"></span>
        <span class="lockup__name">VOLT</span>
      </div>
    </div>
  </section>

</main>
</body>
</html>
```